Business Card Design

I need a business card for my resume writing business. I have a logo that Im not keen on anymore so I would like the business card to use my photo instead of a logo. I am for mid career and trades resumes and prefer not to do executive resumes so don't need to aim for exectives. I would like it to be colourful. I like bright sky blue and maybe some pink or purple but primarily bright sky blue. I don't like green and Im keen see a fair bit of white on the card. As I have a photo to go it, it will need to go on a white background.

Target Market(s)

mid range careers. Not executives

Industry/Entity Type

Business

Contact Information for Business Card

Wyn Marchetti
Resume Writer
Clear Path CVs
27 The Lanyard
HARWOOD NSW 2465
wyn@clearpathcvs.com.au
0417362958
www.clearpathcvs.com.au

Requirements
Nice to have
• Maybe colours similar to my website - www.clearpathcvs.com.au but not with any black on it.
Should not have
• No green or dark colours

```html
<!DOCTYPE html>
<html lang="en">
<head>
<meta charset="utf-8">
<title>Clear Path CVs – Business Card</title>
<link rel="stylesheet" href="https://fonts.googleapis.com/css2?family=Questrial&family=Poppins:wght@600&display=swap">
<style>
  :root {
    --sky: #2ba8df;
    --white: #ffffff;
    --page: #f3f4f6;
    --ink: #2e2e2e;
    --ink-soft: #3c3c3c;
    --photo-light: #eeeae6;
    --photo-mid: #d9c3b4;
    --photo-dark: #6b4434;
  }
  * { box-sizing: border-box; margin: 0; padding: 0; }
  html, body {
    width: 1200px;
    height: 780px;
    overflow: hidden;
    background: var(--page);
  }
  .card {
    position: absolute;
    left: 96px;
    top: 99px;
    width: 1003px;
    height: 558px;
    background: var(--white);
    border-radius: 31px;
    overflow: hidden;
    font-family: "Questrial", "Century Gothic", sans-serif;
    color: var(--ink-soft);
  }
  .portrait {
    position: absolute;
    left: 42px;
    top: 58px;
    width: 276px;
    height: 391px;
    background:
      radial-gradient(ellipse 45% 40% at 50% 32%, var(--photo-mid) 0%, rgba(217,195,180,0) 100%),
      radial-gradient(ellipse 55% 45% at 50% 25%, var(--photo-dark) 0%, rgba(107,68,52,0) 100%),
      linear-gradient(180deg, var(--photo-light) 0%, #f6f4f1 60%, #ffffff 100%);
  }
  .brand-name {
    position: absolute;
    right: 84px;
    top: 62px;
    font-size: 38px;
    color: var(--sky);
    letter-spacing: 0.5px;
    white-space: nowrap;
  }
  .identity {
    position: absolute;
    left: 347px;
    top: 150px;
  }
  .person-name {
    font-family: "Poppins", "Century Gothic", sans-serif;
    font-weight: 600;
    font-size: 25px;
    line-height: 34px;
    color: var(--ink);
  }
  .person-role {
    font-size: 28px;
    line-height: 38px;
    color: var(--ink-soft);
  }
  .contacts {
    position: absolute;
    left: 349px;
    top: 283px;
    list-style: none;
  }
  .contacts li {
    display: flex;
    align-items: center;
    height: 42px;
    font-size: 26px;
    color: var(--ink-soft);
    white-space: nowrap;
  }
  .contacts svg {
    width: 32px;
    height: 28px;
    margin-right: 24px;
    flex: none;
  }
  .rule {
    position: absolute;
    left: 0;
    top: 449px;
    width: 100%;
    height: 5px;
    background: var(--sky);
  }
  .phone-band {
    position: absolute;
    left: 0;
    top: 463px;
    width: 100%;
    height: 95px;
    background: var(--sky);
    display: flex;
    align-items: center;
    padding-left: 349px;
    color: var(--white);
  }
  .phone-band svg {
    width: 27px;
    height: 42px;
    margin-right: 31px;
  }
  .phone-number {
    font-family: "Poppins", "Century Gothic", sans-serif;
    font-weight: 600;
    font-size: 40px;
    letter-spacing: 0.5px;
  }
</style>
</head>
<body>
  <main class="card">
    <div class="portrait" role="img" aria-label="Portrait photo of Wyn Marchetti"></div>

    <div class="brand-name">Clear Path CVs</div>

    <div class="identity">
      <h1 class="person-name">Wyn Marchetti</h1>
      <p class="person-role">Resume Writer</p>
    </div>

    <ul class="contacts">
      <li>
        <svg viewBox="0 0 32 28" aria-hidden="true">
          <rect x="2" y="5" width="28" height="18" rx="1.5" fill="none" stroke="var(--sky)" stroke-width="2.4"/>
          <path d="M2.5 6 L16 16 L29.5 6" fill="none" stroke="var(--sky)" stroke-width="2.4"/>
        </svg>
        wyn@clearpathcvs.com.au
      </li>
      <li>
        <svg viewBox="0 0 32 28" aria-hidden="true">
          <circle cx="16" cy="14" r="12" fill="none" stroke="var(--sky)" stroke-width="2.2"/>
          <ellipse cx="16" cy="14" rx="5.5" ry="12" fill="none" stroke="var(--sky)" stroke-width="2"/>
          <line x1="4" y1="14" x2="28" y2="14" stroke="var(--sky)" stroke-width="2"/>
          <path d="M6 8 H26 M6 20 H26" stroke="var(--sky)" stroke-width="1.8"/>
        </svg>
        www.clearpathcvs.com.au
      </li>
      <li>
        <svg viewBox="0 0 32 28" aria-hidden="true">
          <path d="M16 2 L30 11 H2 Z" fill="var(--sky)"/>
          <rect x="5" y="12" width="22" height="14" fill="var(--sky)"/>
          <rect x="12.5" y="16" width="7" height="10" fill="var(--white)"/>
        </svg>
        27 The Lanyard HARWOOD NSW 2465
      </li>
    </ul>

    <div class="rule"></div>

    <div class="phone-band">
      <svg viewBox="0 0 27 42" aria-hidden="true">
        <rect x="2" y="2" width="23" height="38" rx="4" fill="none" stroke="var(--white)" stroke-width="3"/>
        <rect x="6" y="7" width="15" height="24" fill="var(--white)"/>
        <circle cx="13.5" cy="35.5" r="1.8" fill="var(--white)"/>
      </svg>
      <span class="phone-number">0417362958</span>
    </div>
  </main>
</body>
</html>
```